Campaign Sign

I'm looking for a design I can use on 18" x 24" yard signs for my campaign. The attachment is something I've been considering but not sold on.
I would like see the "X" in the voter box stylized. Either with paintbrush, made into a check mark through an X, etc.

I'm also open to going a different direction if I see something I like more.

I'll need a small amount or room at the bottom to the required campaign disclaimer.

Logo Text

Marla Quenby District 2

```html
<!DOCTYPE html>
<html lang="en">
<head>
<meta charset="utf-8">
<title>Marla Quenby – District 2 Yard Sign</title>
<link href="https://fonts.googleapis.com/css2?family=Bitter:wght@800&family=Archivo:ital,wght@0,700;1,500&display=swap" rel="stylesheet">
<style>
  :root {
    --navy: #0f3350;
    --red: #be1e2e;
    --white: #ffffff;
  }
  html, body {
    margin: 0;
    padding: 0;
    width: 1200px;
    height: 900px;
    overflow: hidden;
    background: var(--navy);
  }
  .sign {
    position: relative;
    width: 1200px;
    height: 900px;
    background: var(--navy);
    color: var(--white);
  }
  .candidate {
    margin: 0;
    font-family: "Bitter", serif;
    font-weight: 800;
  }
  .candidate-first {
    position: absolute;
    top: 91px;
    left: 0;
    width: 1056px;
    text-align: center;
    font-size: 178px;
    line-height: 1;
    letter-spacing: 2px;
  }
  .candidate-last {
    position: absolute;
    top: 256px;
    left: 68px;
    font-size: 225px;
    line-height: 1;
  }
  .vote-square {
    position: absolute;
    top: 291px;
    left: 918px;
    width: 174px;
    height: 174px;
    background: var(--red);
  }
  .district-band {
    position: absolute;
    top: 551px;
    left: 0;
    width: 1200px;
    height: 180px;
    background: var(--red);
    display: flex;
    align-items: center;
    justify-content: center;
  }
  .district-label {
    margin: 0;
    font-family: "Archivo", sans-serif;
    font-weight: 700;
    font-size: 92px;
    letter-spacing: 0.14em;
    margin-right: -0.14em;
    line-height: 1;
  }
  .disclaimer {
    position: absolute;
    top: 757px;
    left: 0;
    right: 0;
    margin: 0;
    text-align: center;
    font-family: "Archivo", sans-serif;
    font-style: italic;
    font-weight: 500;
    font-size: 31px;
    line-height: 1.2;
  }
</style>
</head>
<body>
  <main class="sign">
    <h1 class="candidate">
      <span class="candidate-first">Marla</span>
      <span class="candidate-last">Quenby</span>
    </h1>
    <div class="vote-square" aria-hidden="true"></div>
    <div class="district-band">
      <p class="district-label">DISTRICT 2</p>
    </div>
    <p class="disclaimer">Paid for by Marla Quenby for District 2 218 Larkspur Lane Oakridge, AL 35999</p>
  </main>
</body>
</html>
```